Book Postcard Design

We need a postcard design to promote the book written by our founder and president, Lior Beckett. The book is titled KESTRL: The Craft and Logic of Momentum. We're open to any eye-catching image designs you come up with.

```html
<!DOCTYPE html>
<html lang="en">
<head>
<meta charset="utf-8">
<title>A New Generation of Change – Postcard</title>
<link href="https://fonts.googleapis.com/css2?family=Open+Sans:ital,wght@0,400;0,600;0,700;1,700&family=Montserrat:wght@400&display=swap" rel="stylesheet">
<style>
  :root{
    --page:#e9e6e2;
    --night:#1b1a24;
    --violet:#5a3f84;
    --violet-soft:#6d4f99;
    --lavender:#e4d6ef;
    --ink:#3a3a3e;
    --panel:#efeff0;
    --rule:#b9b9bd;
    --tab-shade:#9b98a0;
  }
  *{box-sizing:border-box;margin:0;padding:0}
  html,body{width:1200px;height:1200px;overflow:hidden;background:var(--page)}
  body{position:relative;font-family:"Open Sans",Arial,sans-serif;color:var(--ink)}

  .card{position:absolute;left:100px;width:1000px;height:545px;box-shadow:0 6px 18px rgba(0,0,0,.22);overflow:hidden}
  .card--front{top:35px}
  .card--back{top:620px;background:#fff}

  .cover-photo{position:absolute;inset:0;
    background:
      radial-gradient(ellipse 30% 70% at 55% 20%,rgba(170,120,200,.55),transparent 70%),
      radial-gradient(ellipse 70% 35% at 60% 82%,rgba(200,110,50,.75),transparent 70%),
      linear-gradient(180deg,#1c1b2a 0%,#2c2540 45%,#5a3d3a 72%,#16151a 88%,#0f0f12 100%);}

  .title-frame{position:absolute;left:170px;top:160px;width:660px;height:200px;border:3px solid var(--lavender);
    display:flex;align-items:center;justify-content:center;text-align:center}
  .title{font-family:"Montserrat",Arial,sans-serif;font-weight:400;color:var(--lavender);font-size:58px;line-height:1.08;letter-spacing:1px;text-transform:uppercase}

  .letter{position:absolute;left:28px;top:26px;width:462px;height:470px;background:var(--panel);border-radius:10px;padding:18px 20px;font-size:12.4px;line-height:1.42}
  .letter p{margin-bottom:9px}
  .letter .lead-in{color:var(--violet);font-weight:700;display:block}
  .letter .book{font-weight:700;font-style:italic}
  .letter .link{color:var(--violet)}
  .letter .phone{color:var(--violet);display:inline-flex;align-items:center;gap:5px}
  .letter .sign{margin-top:14px;font-weight:600}

  .about{position:absolute;left:515px;top:26px;width:460px}
  .about-block{margin-bottom:24px}
  .about-head{display:flex;align-items:flex-end;border-bottom:1px solid var(--rule);margin-bottom:6px}
  .about-tab{background:var(--violet);color:#fff;font-weight:700;font-size:11.5px;letter-spacing:.4px;padding:3px 9px;text-transform:uppercase}
  .about-tab-edge{width:12px;height:21px;background:var(--tab-shade);clip-path:polygon(0 0,40% 0,100% 100%,0 100%)}
  .about-text{font-size:12.4px;line-height:1.45}

  .footer-band{position:absolute;left:0;right:0;bottom:0;height:28px;background:linear-gradient(90deg,#1b1a24,#2a2637 60%,#1b1a24)}
</style>
</head>
<body>

<section class="card card--front">
  <div class="cover-photo" role="img" aria-label="Night sky with the Milky Way over a dark hillside, a lone figure standing on a rock against an orange horizon glow"></div>
  <div class="title-frame">
    <h1 class="title">A New Generation<br>of Change</h1>
  </div>
</section>

<section class="card card--back">
  <article class="letter">
    <p>At The Halvard Group, we believe—actually, we know—that the key to effective leadership is the ability to influence.</p>
    <p><span class="lead-in">Think about it:</span>if you want to enact change in your business, you can't do it alone; you have to recruit and rally all of your employees behind the cause. But your employees are adults, which means getting them to change can be quite the feat indeed.</p>
    <p>Over the years, we've worked with thousands of businesses, and we came to realize just how important (and challenging) the skill of adult behavior change actually is. Those experiences led us to refine the KESTRL methodology for influencing adult behavior, which in turn led to the book you now hold in your hands, <span class="book">KESTRL: The Craft and Logic of Momentum.</span></p>
    <p>We thought you'd appreciate KESTRL, and maybe even glean some fresh insights for your own leadership role. KESTRL is also the methodology at the core of all our products here at The Halvard Group, so if you like the book, be sure to give our website a gander, too (that's at <span class="link">HalvardGroup.net</span>).</p>
    <p>We'd love to chat about the perils, pitfalls, &amp; positives of leadership with you, from one leader to another. <strong>Give us a call at</strong>
      <span class="phone"><svg width="13" height="13" viewBox="0 0 14 14" aria-hidden="true"><circle cx="7" cy="7" r="6.2" fill="none" stroke="currentColor" stroke-width="1"/><path d="M4.6 3.8l1.2-.3.7 1.7-.7.6a4.5 4.5 0 0 0 2 2l.6-.7 1.7.7-.3 1.2c-2.6.2-5.4-2.6-5.2-5.2z" fill="currentColor"/></svg>1-800-555-0182.</span></p>
    <p class="sign">Happy Reading!<br>Lior Beckett/The Halvard Group Team</p>
  </article>

  <div class="about">
    <div class="about-block">
      <div class="about-head"><span class="about-tab">Who we are</span><span class="about-tab-edge"></span></div>
      <p class="about-text">We are The Halvard Group, a charmingly incongruous and blatantly genuine group of big thinkers and list makers. Get us together, and our ideas bloom into vibrant, sky-high projects; take us apart, and we work methodically and assiduously to accomplish the goals we created together. We say there's no mountain too high or ambition too big, for us or our clients.</p>
    </div>
    <div class="about-block">
      <div class="about-head"><span class="about-tab">What we do</span><span class="about-tab-edge"></span></div>
      <p class="about-text">We create and implement practical courses &amp; curriculum to help businesses and individuals grow. With a varied team of experienced coaches and analyzers, we help diagnose and alleviate obstacles in both business-to-business and business-to-consumer enterprises across dozens of industries in order to increase profits and actualize a comprehensive vision for their business.</p>
    </div>
    <div class="about-block">
      <div class="about-head"><span class="about-tab">Why we do it</span><span class="about-tab-edge"></span></div>
      <p class="about-text">We believe that, when outfitted with the right tools, every business can succeed. We believe that the most decisive factor in that success is effective leadership. And we believe that we're the organization that can help every business, regardless of size or industry, change, learn and grow through strong leadership, a clear vision, and a little elbow grease.</p>
    </div>
  </div>

  <div class="footer-band" role="img" aria-label="Starry night sky strip"></div>
</section>

</body>
</html>
```